International Distribution and racing team needs a new business card design.

We need business card, A5 notepad, letter head.
Our business brand name is Veldomarzo and the logo is attached. The Veldomarzo logo is always to be front and centre.
We are a Professional Racing team and international Distribution business in the Go-Karting industry. it is essential that on our stationary that all the brands we distribute are Visible.

Industry/Entity Type

Business

Requirements
Must have
• Veldomarzo LOGO..

```html
<!DOCTYPE html>
<html lang="en">
<head>
<meta charset="utf-8">
<title>Veldomarzo – Business Card</title>
<link href="https://fonts.googleapis.com/css2?family=Lato:wght@400;700;900&display=swap" rel="stylesheet">
<style>
  :root {
    --backdrop: #1c1c1c;
    --card: #2a2b2d;
    --logo: #d6d7d9;
    --text: #f2f2f2;
    --accent: #d4262c;
    --muted: #b9babc;
  }
  * { margin: 0; padding: 0; box-sizing: border-box; }
  html, body {
    width: 1189px; height: 1200px; overflow: hidden;
    background: var(--backdrop);
    font-family: "Lato", sans-serif;
  }
  .card {
    position: absolute; left: 171px;
    width: 855px; height: 487px;
    background: var(--card);
  }
  .card--front { top: 68px; }
  .card--back { top: 627px; }
  .brand-name {
    position: absolute;
    font-weight: 900; color: var(--logo);
    letter-spacing: 2px; line-height: 1;
  }
  .card--front .brand-name {
    left: 0; right: 0; top: 195px; text-align: center; font-size: 86px;
  }
  .card--back .brand-name {
    left: 40px; top: 88px; font-size: 86px;
  }
  .person { position: absolute; left: 42px; top: 268px; }
  .person__name { font-weight: 700; font-size: 27px; color: var(--text); letter-spacing: .5px; line-height: 1; }
  .person__role { font-size: 21px; color: var(--accent); margin-top: 2px; }
  .contacts { position: absolute; left: 42px; top: 356px; list-style: none; }
  .contacts li {
    display: flex; align-items: center; gap: 12px;
    font-size: 21px; color: var(--text); height: 32px;
  }
  .contacts svg { width: 22px; height: 22px; fill: var(--accent); flex: none; }
  .partners {
    position: absolute; left: 505px; top: 292px; width: 315px;
    display: grid; grid-template-columns: 1fr auto; row-gap: 30px; column-gap: 14px;
    align-items: center;
  }
  .partner { font-weight: 700; font-size: 17px; color: var(--muted); white-space: nowrap; display: flex; align-items: center; gap: 7px; }
  .partner--red { color: var(--accent); }
  .partner__mark { width: 12px; height: 12px; background: currentColor; }
  .partners__row3 { grid-column: 1 / 3; display: flex; justify-content: space-between; }
</style>
</head>
<body>
  <section class="card card--front">
    <div class="brand-name">VELDOMARZO</div>
  </section>

  <section class="card card--back">
    <div class="brand-name">VELDOMARZO</div>

    <div class="person">
      <div class="person__name">MARCO BELLINI</div>
      <div class="person__role">Managing director</div>
    </div>

    <ul class="contacts">
      <li>
        <svg viewBox="0 0 24 24" aria-hidden="true"><path d="M3 8c0-2 4-4 9-4s9 2 9 4v2h-5V8H8v2H3z"/><path d="M6 11h12l2 8H4z"/></svg>
        +61 400 555 018
      </li>
      <li>
        <svg viewBox="0 0 24 24" aria-hidden="true"><path d="M2 5h20v14H2z M3.5 6.5 12 13l8.5-6.5" stroke="#2a2b2d" stroke-width="1.5"/></svg>
        info@veldomarzo-mail.com
      </li>
      <li>
        <svg viewBox="0 0 24 24" aria-hidden="true"><circle cx="12" cy="12" r="10"/><path d="M2 12h20M12 2v20M5 6h14M5 18h14M12 2c-5 5-5 15 0 20M12 2c5 5 5 15 0 20" stroke="#2a2b2d" stroke-width="1.2" fill="none"/></svg>
        www.veldomarzo.com
      </li>
    </ul>

    <div class="partners">
      <span class="partner">ARCADIA KART</span>
      <span class="partner partner--red"><span class="partner__mark"></span>BREZZA OILS</span>
      <span class="partner partner--red">TORNIO KARTS</span>
      <span class="partner">STELLA TYRES</span>
      <div class="partners__row3">
        <span class="partner">CORVO</span>
        <span class="partner"><span class="partner__mark"></span>LUMO</span>
        <span class="partner partner--red">FALCO RACING</span>
      </div>
    </div>
  </section>
</body>
</html>
```